依頼詳細
A2の片面4色のポスターのデザインをお願いします。社内の掲示板等に掲示する予定です。健康的で楽しく、さわやかなイメージにするとともに、興味のない人の目を引くことができるようにしたいと思います。イラストではなく、写真を使用するイメージです。

参加しやすくなるように「もらなく参加賞がもらえる」「歩くだけでなくスポーツを歩数換算できる」点を伝えてください。
記載項目
タイトル・募集要項(キャンペーン概要)・健保名・キャッチ等

原稿データを添付いたします。
簡単なラフも添付しますが、ラフに縛られずに作業ください。
サイズ
A2
ページ数
片面
希望イメージ
シンプル 複雑
単色 カラフル
暗い 明るい
日常 高級
遊び心 厳粛
未来的 伝統的
女性的 男性的
希望する色
赤系、水色系、緑系
納品ファイル
補足説明

先方に提案したところ、当選案に決まりました。

皆様、素敵なご提案ありがとうございます。いただいたカンプに関して、他の健保様にも提案していこうと思います。別途ご相談する機会があるかもしれませんがその際はご協力いただければと思います。ありがとうございました。

```html
<!DOCTYPE html>
<html lang="ja">
<head>
<meta charset="utf-8">
<title>いきいきウォーキングキャンペーン</title>
<link rel="stylesheet" href="https://fonts.googleapis.com/css2?family=M+PLUS+Rounded+1c:wght@500;800;900&family=Noto+Sans+JP:wght@400;700;900&display=swap">
<style>
:root{
  --sky:#1ea0e2;
  --navy:#0b3f86;
  --deep:#0a5fa8;
  --green:#3aa835;
  --orange:#f39a1e;
  --ink:#222;
  --paper:#ffffff;
  --pale:#e8f4fb;
}
*{margin:0;padding:0;box-sizing:border-box}
html,body{width:853px;height:1200px;overflow:hidden;background:var(--paper)}
.poster{position:relative;width:853px;height:1200px;overflow:hidden;font-family:"Noto Sans JP",sans-serif;color:var(--ink);background:var(--paper)}
.sky{position:absolute;left:0;top:0;width:853px;height:700px;background:var(--sky)}
.photo{position:absolute;left:0;top:690px;width:853px;height:450px;background:linear-gradient(180deg,#ffffff 0%,#eef3f6 55%,#d9e2e8 100%)}
.title{position:absolute;left:28px;top:26px;font-family:"M PLUS Rounded 1c",sans-serif;font-weight:900;color:#fff;line-height:1;paint-order:stroke fill;-webkit-text-stroke:10px var(--navy)}
.title span{display:block;letter-spacing:-2px}
.title .t1{font-size:62px}
.title .t2{font-size:84px;margin-top:14px}
.title .t3{font-size:84px;margin-top:10px}
.bubble{position:absolute;display:flex;align-items:center;justify-content:center;text-align:center;background:var(--green);color:#fff;border-radius:50%;font-family:"M PLUS Rounded 1c",sans-serif;font-weight:800;font-size:30px;line-height:1.25;border:4px solid #fff}
.bubble.sports{left:525px;top:26px;width:300px;height:132px}
.bubble.prize{left:568px;top:160px;width:257px;height:120px}
.effects{position:absolute;left:24px;top:318px;width:400px;height:380px;background:var(--paper);border-radius:18px;padding:18px 18px}
.effects h2{font-family:"M PLUS Rounded 1c",sans-serif;font-weight:800;color:var(--green);font-size:25px;transform:rotate(-6deg);margin:4px 0 18px 20px}
.effect{display:flex;align-items:flex-start;gap:14px;margin-bottom:20px}
.tag{flex:none;width:62px;height:62px;border-radius:10px;color:#fff;font-weight:900;font-size:17px;line-height:1.15;display:flex;align-items:center;justify-content:center;text-align:center}
.tag.green{background:var(--green)}
.tag.orange{background:var(--orange)}
.tag.red{background:#e2483b}
.effect h3{font-family:"M PLUS Rounded 1c",sans-serif;font-weight:900;color:var(--deep);font-size:30px;line-height:1.1}
.effect p{font-size:13px;line-height:1.45;margin-top:4px}
.outline{position:absolute;left:440px;top:318px;width:389px;background:var(--paper);border-radius:14px;padding:14px 14px 16px}
.outline h2{background:var(--deep);color:#fff;font-size:22px;font-weight:900;padding:6px 14px;border-radius:8px;margin-bottom:8px}
.outline table{width:100%;border-collapse:separate;border-spacing:0 5px;font-size:15px}
.outline th{width:88px;background:var(--sky);color:#fff;font-size:13px;font-weight:700;padding:6px 4px;border-radius:5px;vertical-align:middle}
.outline td{padding:4px 8px;line-height:1.45;border-bottom:1px dotted #9bb}
.outline td.big{font-weight:900;font-size:20px;color:var(--deep)}
.outline td.small{font-size:12.5px}
.recruit{position:absolute;left:612px;top:890px;width:216px;height:216px;border-radius:50%;background:var(--orange);color:#fff;display:flex;align-items:center;justify-content:center;text-align:center;font-family:"M PLUS Rounded 1c",sans-serif;font-weight:900;font-size:44px;line-height:1.2;border:5px solid #fff}
.footer{position:absolute;left:0;top:1140px;width:853px;height:60px;display:flex;align-items:center;justify-content:center;font-size:22px;font-weight:700;letter-spacing:2px}
</style>
</head>
<body>
<div class="poster">
  <div class="sky"></div>
  <div class="photo" role="img" aria-label="白い背景に立つ数羽のペンギンの写真"></div>

  <h1 class="title"><span class="t1">いきいき</span><span class="t2">ウォーキング</span><span class="t3">キャンペーン</span></h1>

  <div class="bubble sports">各種スポーツも<br>歩数換算OK</div>
  <div class="bubble prize">もれなく<br>賞品を進呈</div>

  <section class="effects">
    <h2>歩くってこんなに効きめ！</h2>
    <div class="effect">
      <div class="tag green">気分<br>爽快</div>
      <div><h3>リフレッシュ</h3><p>歩くことで運動だけでなく、気分転換にもなります。</p></div>
    </div>
    <div class="effect">
      <div class="tag orange">老化<br>予防</div>
      <div><h3>アンチエイジング</h3><p>年齢に負けない体力づくりで、若々しさを保ちましょう。</p></div>
    </div>
    <div class="effect">
      <div class="tag red">脂肪<br>燃焼</div>
      <div><h3>アンチメタボ</h3><p>内臓脂肪を燃焼してメタボリックシンドロームを予防できます。</p></div>
    </div>
  </section>

  <section class="outline">
    <h2>キャンペーン概要</h2>
    <table>
      <tr><th>実施内容</th><td class="small">1日平均1万歩以上、2ヶ月で60万歩以上を目標に、歩くことやスポーツを楽しみながら健康づくりに取り組みましょう。</td></tr>
      <tr><th>対象者</th><td class="small">○○○○健康保険組合の被保険者</td></tr>
      <tr><th>募集期間</th><td class="big">8月21日(木)～9月10日(水)</td></tr>
      <tr><th>記録期間</th><td class="big">10月1日(水)～11月30日(土)</td></tr>
      <tr><th>申込方法</th><td class="small">所定の参加申込書に必要事項を記入し、担当窓口までご提出ください。期間中は歩数を記録し、終了後に記録表を提出してください。</td></tr>
      <tr><th>賞品</th><td class="small">達成賞(60万歩以上)<br>努力賞(40万歩以上)</td></tr>
    </table>
  </section>

  <div class="recruit">参加者<br>募集!</div>

  <footer class="footer">○○○○健康保険組合</footer>
</div>
</body>
</html>
```